hair salon business Card Design

My business name is Hair & Beauty @ Corrabin I want a Hot Pink and black business card with a loyalty program on the back after every 2nd haircut the third has $5 off and I will whole punch the squares My business phone number is (07) 54 913 668 address is Shop 2 3/9 Wollard st Corrabin Qld 4571 find us on Circlet should be on the card somewhere with the Circlet logo also a space alocated for your next appointment date n time also would like your har stylists name is Tess on the card somewhere easy to read you can check out my Circlet site for images of my logo n shop signage

Industry/Entity Type

Hair

```html
<!DOCTYPE html>
<html lang="en">
<head>
<meta charset="utf-8">
<title>Hair &amp; Beauty @ Corrabin – Business Card</title>
<link rel="stylesheet" href="https://fonts.googleapis.com/css2?family=Nunito:ital,wght@0,700;0,900;1,800;1,900&family=Kaushan+Script&display=swap">
<style>
  :root {
    --hot-pink: #e0218a;
    --pink-deep: #b81470;
    --pink-soft: #f7d3e7;
    --ink: #1c1b1e;
    --ink-soft: #2e2d31;
    --grey: #8d8a90;
    --grey-light: #cfcdd2;
    --white: #ffffff;
    --backdrop: #e6ddd0;
  }
  * { box-sizing: border-box; margin: 0; padding: 0; }
  html, body { width: 1200px; height: 729px; overflow: hidden; }
  body {
    background: var(--backdrop);
    font-family: "Nunito", Arial, sans-serif;
    position: relative;
  }
  .card {
    position: absolute;
    width: 570px;
    height: 325px;
    overflow: hidden;
    box-shadow: 0 6px 18px rgba(0,0,0,.35);
  }

  /* ---------- back of card ---------- */
  .card--back { left: 60px; top: 55px; background: var(--ink); }
  .back__flourish {
    position: absolute; left: 180px; top: 0; width: 390px; height: 228px;
    background: radial-gradient(ellipse at 65% 55%, rgba(140,138,145,.35), rgba(28,27,30,0) 70%);
  }
  .appointment {
    position: absolute; left: 26px; top: 22px; width: 290px;
    border-radius: 8px; overflow: hidden; background: var(--white);
  }
  .appointment__title {
    background: var(--hot-pink); color: var(--white);
    font-weight: 700; font-size: 17px; text-align: center; height: 30px; line-height: 30px;
  }
  .appointment__grid { display: grid; grid-template-columns: 26px repeat(3, 1fr); }
  .appointment__icon {
    background: var(--grey); display: flex; align-items: center; justify-content: center; height: 30px;
  }
  .appointment__cell { border-left: 1px solid var(--pink-soft); height: 30px; }
  .appointment__cell--date { border-bottom: 1px solid var(--pink-soft); }
  .appointment__cell--time {
    background: #fbe9f3; color: var(--hot-pink); font-size: 10px; font-weight: 700;
    line-height: 11px; text-align: right; padding: 4px 14px 0 0;
  }
  .loyalty { position: absolute; left: 360px; top: 20px; width: 190px; }
  .loyalty__slots { display: flex; gap: 12px; margin-left: 18px; }
  .loyalty__slot { position: relative; width: 44px; height: 40px; }
  .loyalty__num {
    position: absolute; right: 0; top: -4px; font-size: 40px; font-weight: 900;
    color: var(--grey); line-height: 1;
  }
  .loyalty__box {
    position: absolute; left: 0; top: 12px; width: 24px; height: 24px;
    background: var(--grey-light); border-radius: 3px; box-shadow: 0 0 4px rgba(0,0,0,.6);
  }
  .loyalty__text {
    margin-top: 10px; color: var(--white); font-weight: 900; font-size: 14px; line-height: 17px; text-align: center;
  }
  .loyalty__text em { font-style: normal; color: var(--hot-pink); }
  .stylist { position: absolute; left: 108px; top: 148px; font-style: italic; font-weight: 900; }
  .stylist__lead { color: var(--white); font-size: 22px; line-height: 24px; }
  .stylist__name { color: var(--hot-pink); font-size: 30px; line-height: 30px; margin-left: 44px; }
  .back__band {
    position: absolute; left: 0; bottom: 0; width: 100%; height: 97px;
    background: linear-gradient(var(--hot-pink), var(--pink-deep));
  }
  .business-name { color: var(--white); font-weight: 900; line-height: 1; white-space: nowrap; }
  .business-name--small { position: absolute; left: 26px; top: 36px; font-size: 19px; }
  .social { position: absolute; left: 290px; top: 18px; color: var(--white); }
  .social__lead { font-family: "Kaushan Script", cursive; font-size: 20px; line-height: 24px; }
  .social__page { display: flex; align-items: center; gap: 6px; font-weight: 900; font-size: 15px; margin-top: 4px; }
  .social__mark { width: 12px; height: 12px; background: var(--white); display: inline-block; }

  /* ---------- front of card ---------- */
  .card--front { left: 570px; top: 395px; background: linear-gradient(160deg, #ea3d99, var(--hot-pink) 45%, var(--pink-deep)); }
  .front__flourish {
    position: absolute; left: 0; top: 0; width: 570px; height: 215px;
    background: radial-gradient(ellipse at 82% 20%, rgba(255,255,255,.22), rgba(255,255,255,0) 55%),
                radial-gradient(ellipse at 12% 60%, rgba(255,255,255,.16), rgba(255,255,255,0) 45%);
  }
  .business-name--large { position: absolute; left: 0; top: 88px; width: 100%; text-align: center; font-size: 40px; }
  .front__band {
    position: absolute; left: 0; bottom: 0; width: 100%; height: 110px;
    background: linear-gradient(var(--ink-soft), var(--ink));
  }
  .contact-rail {
    position: absolute; left: 24px; top: 12px; width: 26px; height: 86px;
    background: linear-gradient(90deg, #d9d7dc, var(--white)); border-radius: 4px;
    display: flex; flex-direction: column; align-items: center; gap: 10px; padding-top: 8px;
  }
  .contact-rail__icon {
    width: 20px; height: 20px; border-radius: 50%; background: var(--hot-pink);
    display: flex; align-items: center; justify-content: center;
  }
  .contact { position: absolute; left: 68px; top: 16px; color: var(--white); font-weight: 900; font-style: italic; font-size: 17px; line-height: 30px; }
</style>
</head>
<body>

<section class="card card--back" aria-label="Back of business card">
  <div class="back__flourish" role="img" aria-label="Soft grey swirl flourish decoration"></div>

  <div class="appointment">
    <div class="appointment__title">your next appointment</div>
    <div class="appointment__grid">
      <div class="appointment__icon">
        <svg width="14" height="14" viewBox="0 0 14 14" aria-hidden="true">
          <rect x="1" y="2" width="12" height="11" fill="none" stroke="#1c1b1e" stroke-width="1.5"/>
          <rect x="1" y="2" width="12" height="3" fill="#1c1b1e"/>
          <path d="M4 7h2v2H4zM8 7h2v2H8zM4 10h2v2H4zM8 10h2v2H8z" fill="#1c1b1e"/>
        </svg>
      </div>
      <div class="appointment__cell appointment__cell--date"></div>
      <div class="appointment__cell appointment__cell--date"></div>
      <div class="appointment__cell appointment__cell--date"></div>
      <div class="appointment__icon">
        <svg width="14" height="14" viewBox="0 0 14 14" aria-hidden="true">
          <circle cx="7" cy="7" r="5.5" fill="#fff" stroke="#1c1b1e" stroke-width="1.5"/>
          <path d="M7 4v3.2l2 1.4" fill="none" stroke="#1c1b1e" stroke-width="1.4"/>
        </svg>
      </div>
      <div class="appointment__cell appointment__cell--time">pm<br>am</div>
      <div class="appointment__cell appointment__cell--time">pm<br>am</div>
      <div class="appointment__cell appointment__cell--time">pm<br>am</div>
    </div>
  </div>

  <div class="loyalty">
    <div class="loyalty__slots">
      <div class="loyalty__slot"><span class="loyalty__num">1</span><span class="loyalty__box"></span></div>
      <div class="loyalty__slot"><span class="loyalty__num">2</span><span class="loyalty__box"></span></div>
      <div class="loyalty__slot"><span class="loyalty__num">3</span><span class="loyalty__box"></span></div>
    </div>
    <p class="loyalty__text">after every 2nd haircut<br>the third has <em>$5 off</em></p>
  </div>

  <div class="stylist">
    <p class="stylist__lead">your hair stylists</p>
    <p class="stylist__name">name is Tess</p>
  </div>

  <div class="back__band">
    <p class="business-name business-name--small">Hair &amp; Beauty @ Corrabin</p>
    <div class="social">
      <p class="social__lead">find us on Circlet</p>
      <p class="social__page"><span class="social__mark"></span>Hair &amp; Beauty at Corrabin</p>
    </div>
  </div>
</section>

<section class="card card--front" aria-label="Front of business card">
  <div class="front__flourish" role="img" aria-label="Soft pink swirl flourish decoration"></div>
  <p class="business-name business-name--large">Hair &amp; Beauty @ Corrabin</p>
  <div class="front__band">
    <div class="contact-rail">
      <span class="contact-rail__icon">
        <svg width="12" height="12" viewBox="0 0 12 12" aria-hidden="true">
          <path d="M2.5 1h2l1 2.5-1.3 1a6 6 0 0 0 3.3 3.3l1-1.3 2.5 1v2a1 1 0 0 1-1 1A9.5 9.5 0 0 1 1.5 2a1 1 0 0 1 1-1z" fill="#fff"/>
        </svg>
      </span>
      <span class="contact-rail__icon">
        <svg width="12" height="12" viewBox="0 0 12 12" aria-hidden="true">
          <path d="M6 1.5 1 6h1.5v4.5h2.5V7.5h2v3h2.5V6H11z" fill="#fff"/>
        </svg>
      </span>
    </div>
    <div class="contact">
      <p>(07) 54 913 668</p>
      <p>Shop 2 3/9 Wollard st Corrabin Qld 4571</p>
    </div>
  </div>
</section>

</body>
</html>
```